website conversion to Wordpress with an updated look and feel

Bright Torque Hub Limited is a company and an online presence, which promotes and sells a branded fuel additive product named “Valmix”.

The existing website is at www.brighttorquehub.co.uk

The site consists of static but attractive pages, a contact form, and most importantly a shopping page which is driven externally using shopvarn.com. Therefore e-commerce coding is NOT required as this task is performed by shopvarn via a plugin.

The website is 4 years old and we intend to revamp the graphics and the image of the company and the website to give it a modern “Windows 10” look!

Less text and less cluttering, Cleaner and easier navigations, bigger and clearer fonts. Simple message to put across to visitors/potential customers. Be creative.

The site needs to be simplified - the detail can/should still be there... But it can be placed deeper down or hidden by the use of dropdowns, callouts, etc.

A couple of good example styles we like are

https://www.brolavent.com/
http://www.4plumtoaster.com/en/#/welcome
https://www.tivoramp.com/

Some specific areas of attention.

homepage - This needs to really reflect the new look-and feel of the website. In addition the product we sell can be used in a number of applications - currently navigation to these different applications is through the moving banner. This needs to be changed. The major areas for access should be

Heating Oil
Vehicles
Marine
Generators

Technical requirements what we want:-
Wordpress (self hosted ) - currently Joomla based
Use of webfonts to improve typographic appearances
Shopvarn integration using plugin
Pagewall/Twitter integration
Responsive design (Mobile friendly)
Search Engine friendly and some SEO optimisation
Google Analytics / Bing webmaster tracking

Target Market(s)

Owners of Olm branded range cookers and similar - our product fixes a fuel problem specific to these devices.

Also bulk fuel users looking to save money on their fuel costs - product improves fuel efficiency and reduces maintenance.

Industry/Entity Type

E-Commerce

Font styles to use
Sans Serif

Requirements
Must have
• Wordpress design
• Responsive design
• Simple "clean" look and feel
• Use of stock graphics
• a review of all current pages
Nice to have
• Social media integration - blog
• A forum to discuss the product and problems people experience with fuel

```html
<!DOCTYPE html>
<html lang="en">
<head>
<meta charset="utf-8">
<title>Contact Us – Bright Torque Hub</title>
<link rel="stylesheet" href="https://fonts.googleapis.com/css2?family=Open+Sans:wght@300;400;600;700&display=swap">
<style>
:root{
  --page:#ffffff;
  --top-bar:#b8b8b8;
  --panel:#e4e4e4;
  --panel-edge:#c9c9c9;
  --ink:#1a1a1a;
  --rule:#9a9a9a;
  --field:#ffffff;
  --field-hi:#fdf3b9;
  --field-edge:#c4c4c4;
  --btn:#3b3b3b;
  --green:#8fd160;
  --green-text:#8fcf5b;
  --footer-head:#2b2b2b;
  --footer:#000000;
  --footer-muted:#8c8c8c;
  --footer-field:#bdbdbd;
  --widget:#4a4a4a;
  --widget-head:#6a8bd6;
  --map-light:#e6e6e6;
  --map-dark:#d2d2d2;
}
*{box-sizing:border-box;margin:0;padding:0}
html,body{width:1200px;height:1151px;overflow:hidden;background:var(--page)}
body{position:relative;font-family:"Open Sans",Arial,sans-serif;color:var(--ink)}
.abs{position:absolute}
.top-bar{left:0;top:0;width:1200px;height:18px;background:var(--top-bar)}
.page-title{left:0;top:52px;width:1200px;text-align:center;font-weight:300;font-size:54px;letter-spacing:1px}

.panel{top:176px;height:392px;background:var(--panel);border:2px solid var(--panel-edge)}
.panel-address{left:114px;width:311px}
.panel-form{left:449px;width:310px}
.panel-map{left:788px;width:311px;background:var(--green);border-color:var(--panel-edge)}

.company{left:70px;top:24px;font-size:19.5px;line-height:23px}
.company strong{font-weight:700;display:block}
.rule{left:22px;width:265px;height:1px;background:var(--rule)}
.call{left:68px;top:187px;font-size:18.5px;line-height:22px}
.call strong{font-weight:700}
.note{left:68px;top:271px;width:210px;font-size:14.2px;line-height:17px}
.icon{fill:var(--ink)}

.form-intro{left:24px;top:14px;width:282px;font-size:12.2px;line-height:15px;letter-spacing:-.1px}
.field{left:24px;width:258px;height:28px;background:var(--field);border:2px solid var(--field-edge);font-size:13.5px;padding:3px 9px;line-height:18px}
.field.hi{background:var(--field-hi)}
.field.msg{height:85px}
.select-arrow{right:3px;top:3px;width:18px;height:18px;background:#333}
.check{left:24px;top:314px;width:13px;height:13px;background:var(--field);border:1px solid var(--field-edge)}
.check-label{left:46px;top:311px;font-size:13px}
.submit{left:85px;top:344px;width:132px;height:31px;background:var(--btn);color:#fff;font-weight:700;font-size:17px;text-align:center;line-height:31px;letter-spacing:.5px}

.map{left:15px;top:15px;width:274px;height:357px;background:linear-gradient(160deg,var(--map-light) 0%,var(--map-dark) 100%)}

.footer-line{left:0;top:706px;width:1200px;height:10px;background:var(--green)}
.footer-head{left:0;top:716px;width:1200px;height:50px;background:var(--footer-head)}
.footer{left:0;top:766px;width:1200px;height:341px;background:var(--footer)}
.footer-base{left:0;top:1107px;width:1200px;height:44px;background:var(--footer-head);color:var(--green-text);font-size:12.5px;text-align:center;line-height:44px}
.col-title{top:729px;color:var(--green-text);font-weight:300;font-size:20.5px}

.sub-text{left:112px;top:790px;width:190px;color:var(--footer-muted);font-size:12px;line-height:15px}
.sub-field{left:112px;width:169px;height:22px;background:var(--footer-field);font-size:13px;padding:1px 9px;line-height:20px}
.sub-btn{left:112px;top:904px;width:76px;height:22px;background:var(--green);color:#111;font-weight:700;font-size:13px;text-align:center;line-height:22px}
.privacy{left:109px;top:934px;color:var(--footer-muted);font-size:12px}
.online{left:113px;top:982px;color:var(--footer-muted);font-size:12px}
.social{top:1011px;width:22px;height:22px;border-radius:50%;background:#5c5c5c}

.widget{left:353px;top:795px;width:226px;height:231px;background:var(--widget);border:1px solid #777}
.widget-head{left:0;top:0;width:224px;height:28px;background:var(--widget-head);color:#fff;font-size:11px;font-weight:600;padding:6px 14px}
.widget-mark{left:14px;top:42px;width:26px;height:26px;background:#6c8f4e}
.widget-name{left:52px;top:38px;color:#fff;font-size:12.5px;font-weight:700}
.widget-like{left:52px;top:57px;width:36px;height:17px;background:#ddd;border:1px solid #999;font-size:9px;text-align:center;line-height:15px;color:#333}
.widget-rule{left:10px;top:80px;width:204px;height:1px;background:#777}
.widget-count{left:12px;top:88px;font-size:10.5px;color:#fff}
.widget-count span{color:#8fb0f0}
.people{left:12px;top:103px;width:202px;display:grid;grid-template-columns:repeat(4,46px);gap:5px}
.people div{height:46px}
.widget-foot{left:10px;top:208px;font-size:9.5px;color:#eee}

.links{top:785px;list-style:none;font-size:16.5px;font-weight:300;line-height:24.8px}
.links li{color:var(--footer-muted);text-decoration:underline}
</style>
</head>
<body>
<div class="abs top-bar"></div>
<h1 class="abs page-title">CONTACT US</h1>

<section class="abs panel panel-address">
  <svg class="abs icon" style="left:20px;top:25px" width="28" height="24" viewBox="0 0 28 24"><path d="M14 1 1 12h4v11h7v-7h4v7h7V12h4z"/></svg>
  <div class="abs company"><strong>BRIGHTTORQUEHUB</strong>7 Harwin Court<br>Morrow Lane<br>Kelsford<br>Wendshire<br>KF21 8QZ</div>
  <div class="abs rule" style="top:172px"></div>
  <svg class="abs icon" style="left:24px;top:192px" width="20" height="34" viewBox="0 0 20 34"><path d="M2 0h16a2 2 0 0 1 2 2v30a2 2 0 0 1-2 2H2a2 2 0 0 1-2-2V2a2 2 0 0 1 2-2zm1 4v10h14V4zm1 14v3h3v-3zm5 0v3h3v-3zm5 0v3h3v-3zM4 23v3h3v-3zm5 0v3h3v-3zm5 0v3h3v-3zM4 28v3h3v-3zm5 0v3h3v-3zm5 0v3h3v-3z"/></svg>
  <div class="abs call">Call us FREE :<br><strong>0800 555 0192</strong></div>
  <div class="abs rule" style="top:251px"></div>
  <svg class="abs" style="left:24px;top:277px" width="28" height="26" viewBox="0 0 28 26" fill="none" stroke="#1a1a1a" stroke-width="2.4"><path d="M3 3h16v20H3z"/><path d="M7 9h8M7 13h8M7 17h5"/><path d="M25 4 14 19l-2 4 4-2L27 6z" fill="#1a1a1a"/></svg>
  <p class="abs note">Feel free to use the contact form on the right of the screen to send any email enquiries or questions you may have.</p>
</section>

<section class="abs panel panel-form">
  <p class="abs form-intro">Got a Question about our products or additives in general? Just fill out this short form and we will get back to you!</p>
  <div class="abs field" style="top:74px">Name</div>
  <div class="abs field hi" style="top:110px">Email</div>
  <div class="abs field" style="top:146px">Phone</div>
  <div class="abs field" style="top:183px">Area Of interest
    <svg class="abs select-arrow" viewBox="0 0 18 18"><path d="M4 5h10l-5 8z" fill="#fff"/></svg>
  </div>
  <div class="abs field hi msg" style="top:218px">Message</div>
  <div class="abs check"></div>
  <div class="abs check-label">Send me a Copy</div>
  <div class="abs submit">SUBMIT</div>
</section>

<section class="abs panel panel-map">
  <div class="abs map" role="img" aria-label="Street map showing the office location"></div>
</section>

<div class="abs footer-line"></div>
<div class="abs footer-head"></div>
<div class="abs footer"></div>

<h2 class="abs col-title" style="left:112px">SUBSCRIBE</h2>
<h2 class="abs col-title" style="left:353px">SHARE</h2>
<h2 class="abs col-title" style="left:644px">APPLICATIONS</h2>
<h2 class="abs col-title" style="left:905px">ABOUT VALMIX</h2>

<p class="abs sub-text">Please &nbsp;subscribe for our latest newsletter to your inbox</p>
<div class="abs sub-field" style="top:831px">Name</div>
<div class="abs sub-field" style="top:867px">Email</div>
<div class="abs sub-btn">SUBMIT</div>
<div class="abs privacy">*We respect your Privacy</div>
<div class="abs online">Find us online :</div>
<div class="abs social" style="left:110px"></div>
<div class="abs social" style="left:151px"></div>
<div class="abs social" style="left:193px"></div>
<div class="abs social" style="left:233px"></div>

<aside class="abs widget">
  <div class="abs widget-head">Find us on Pagewall</div>
  <div class="abs widget-mark"></div>
  <div class="abs widget-name">Brighttorquehub</div>
  <div class="abs widget-like">Like</div>
  <div class="abs widget-rule"></div>
  <div class="abs widget-count"><span>72457 people like</span> &nbsp;Brighttorquehub</div>
  <div class="abs people">
    <div role="img" aria-label="Follower photo" style="background:#5a6fa8"></div>
    <div role="img" aria-label="Follower photo" style="background:#4d6b3c"></div>
    <div role="img" aria-label="Follower photo" style="background:#6b5a4a"></div>
    <div role="img" aria-label="Follower photo" style="background:#8aa3b8"></div>
    <div role="img" aria-label="Follower photo" style="background:#8c8478"></div>
    <div role="img" aria-label="Follower photo" style="background:#7a5a55"></div>
    <div role="img" aria-label="Follower photo" style="background:#5f6a8a"></div>
    <div role="img" aria-label="Follower photo" style="background:#3c3436"></div>
  </div>
  <div class="abs widget-foot">Pagewall social plugin</div>
</aside>

<ul class="abs links" style="left:648px">
  <li>Transport</li>
  <li>Heating oil</li>
  <li>Olm and Corrin</li>
  <li>Industry and fuel bunkers</li>
  <li>Fuel saving tips</li>
  <li>Marine and yachting</li>
</ul>
<ul class="abs links" style="left:905px">
  <li>About Valmix</li>
  <li>Contact us</li>
  <li>Downloads</li>
  <li>Online store</li>
  <li>Olm DIY Services</li>
  <li>Milestretch</li>
  <li style="line-height:17px;padding-top:4px">Harlow &amp; Finch - Olm<br>&amp; Corrin specialists</li>
</ul>

<footer class="abs footer-base">COPYRIGHT &nbsp;2015 - BRIGHT TORQUE HUB &nbsp;- ALL RIGHTS RESERVED</footer>
</body>
</html>
```